Construction Company business card and Logo.

We need a business card for a Building Company.
We build and constuction manage.
A simple logo is also required. Ive attached some samples that may assist.
Logo colours: Blue,sunburnt orange,lime/green and brown/grey.
The Font for the Brevanta logo ive been using is Georgia.
Maybe the A in Brevanta can be like my logo design..?
All other font either calibri or arial, something simple.
Simple/modern and neat is what i am looking for.
My card should look organised to convey what the company is about.

Target Market(s)

Developers, architects, proffesionals in general

Industry/Entity Type

Business

Contact Information for Business Card

Brevanta Constructions Pty Ltd
ACN: 381 607 925 Lic:716382D
Dermot Halvorsen
Managing Director
0438 215 706
dermot@brevanta.com.au
www.brevanta.com.au
Industrial.Commercial.Residential.Build Management

Requirements
Must have
• Ive attached some ideas for the logo. Its simple. If you come up with something else, please show me as im not 100% sure of what i want.
The front of the card should be white.
The back of the card should have the company name and logo with Blue background
Should not have
• the design should be simple.
No old style fonts or italics etc

```html
<!DOCTYPE html>
<html lang="en">
<head>
<meta charset="utf-8">
<title>Brevanta Constructions – Business Card</title>
<link href="https://fonts.googleapis.com/css2?family=Gelasio:wght@400&family=Arimo:wght@400&display=swap" rel="stylesheet">
<style>
  :root {
    --card-bg: #ffffff;
    --ink: #231f20;
    --brand-blue: #3f418a;
    --tag-bar: #c8c8ca;
    --rule: #cfcfd1;
  }
  html, body {
    margin: 0;
    padding: 0;
    overflow: hidden;
    background: var(--card-bg);
  }
  .card {
    position: relative;
    width: 1200px;
    height: 1000px;
    background: var(--card-bg);
    color: var(--ink);
    font-family: "Arimo", Arial, sans-serif;
    overflow: hidden;
  }
  .brand-square {
    position: absolute;
    left: 120px;
    top: 262px;
    width: 150px;
    height: 150px;
    background: var(--brand-blue);
  }
  .brand-name {
    position: absolute;
    left: 325px;
    top: 212px;
    margin: 0;
    font-family: "Gelasio", Georgia, serif;
    font-weight: 400;
    font-size: 104px;
    line-height: 1;
    letter-spacing: -1px;
    color: var(--ink);
  }
  .brand-entity {
    position: absolute;
    left: 325px;
    top: 331px;
    margin: 0;
    font-family: "Gelasio", Georgia, serif;
    font-weight: 400;
    font-size: 41px;
    line-height: 1;
    letter-spacing: 0.5px;
  }
  .services {
    position: absolute;
    left: 322px;
    top: 390px;
    width: 475px;
    height: 20px;
    margin: 0;
    padding-left: 2px;
    box-sizing: border-box;
    background: var(--tag-bar);
    font-size: 16px;
    line-height: 20px;
    white-space: nowrap;
  }
  .services .dot {
    display: inline-block;
    width: 12px;
    height: 12px;
    margin: 0 2px 0 3px;
    border-radius: 50%;
    background: var(--ink);
    vertical-align: -1px;
  }
  .person {
    position: absolute;
    right: 86px;
    top: 494px;
    width: 420px;
    text-align: right;
  }
  .person-name {
    margin: 0;
    font-size: 38px;
    font-weight: 400;
    line-height: 1;
    letter-spacing: 0.5px;
    padding-bottom: 10px;
    border-bottom: 1px solid var(--rule);
  }
  .person-role {
    margin: 9px 0 0;
    font-size: 26px;
    line-height: 1;
  }
  .contact {
    position: absolute;
    right: 86px;
    top: 653px;
    margin: 0;
    font-size: 27px;
    line-height: 37px;
    text-align: right;
    font-style: normal;
  }
  .contact .label-email {
    margin-right: 4px;
  }
  .website {
    position: absolute;
    left: 120px;
    top: 690px;
    margin: 0;
    font-size: 27px;
    line-height: 37px;
  }
</style>
</head>
<body>
<main class="card">
  <div class="brand-square" aria-hidden="true"></div>
  <h1 class="brand-name">Brevanta</h1>
  <p class="brand-entity">Constructions Pty Ltd</p>
  <p class="services">Industrial<span class="dot"></span>Commercial<span class="dot"></span>Residential<span class="dot"></span>Build Management</p>

  <section class="person">
    <h2 class="person-name">DERMOT HALVORSEN</h2>
    <p class="person-role">Managing Director</p>
  </section>

  <address class="contact">
    Mobile : 0438 215 706<br>
    <span class="label-email">Email&nbsp;</span>: dermot@brevanta.com.au
  </address>

  <p class="website">www.brevanta.com.au</p>
</main>
</body>
</html>
```